Business Card Design Project for Architecture and Interior Design company

We need a business card design and logo for an architecture and design firm located in Santiago de Chile. It´s a small company, and the name is "Ostrevo" ("Ostr" from my surname Ostrini, and "arq" for arquitectura or architecture. But it would also be nice that the logo comunicates de Word game "Bella" as beautiful in italian, and "arq" as architecture".
The idea is to give a delicate, elegant and sofisticated, yet fresh image. Would prefer grey black and white colors, but wouldn´t mind to use another additional color.
I allready have a web page www.ostrevo-studio.example, but would like to improve the logo design.
Please contact if any further information is requiered.
Reason: Need a more arquitectural and desing spirit in the cards. Few of them give that idea.

```html
<!DOCTYPE html>
<html lang="es">
<head>
<meta charset="utf-8">
<title>Ostrevo — Business Cards</title>
<link rel="stylesheet" href="https://fonts.googleapis.com/css2?family=PT+Sans+Narrow:wght@700&family=Lato:wght@400;700&display=swap">
<style>
  :root {
    --page: #ffffff;
    --ink: #1d1a10;
    --card-edge: #2a2a26;
    --wall-light: #eef0ec;
    --wall-mid: #d3d6d0;
    --floor-light: #f4f1dc;
    --floor-mid: #bfbca6;
    --panel-beige: #ddd9c5;
    --panel-deep: #cdc8b0;
  }
  * { margin: 0; padding: 0; box-sizing: border-box; }
  html, body {
    width: 1200px;
    height: 1000px;
    overflow: hidden;
    background: var(--page);
  }
  .canvas {
    position: relative;
    width: 1200px;
    height: 1000px;
  }
  .card {
    position: absolute;
    border: 1.5px solid var(--card-edge);
    overflow: hidden;
  }
  .card-front {
    left: 40px;
    top: 160px;
    width: 630px;
    height: 372px;
  }
  .card-back {
    left: 524px;
    top: 477px;
    width: 606px;
    height: 343px;
  }
  .room-image {
    position: absolute;
    inset: 0;
  }
  .card-front .room-image {
    background:
      linear-gradient(180deg, var(--wall-light) 0%, var(--wall-mid) 55%, transparent 56%),
      linear-gradient(180deg, var(--floor-mid) 55%, var(--floor-light) 100%);
  }
  .card-back .room-image {
    background:
      linear-gradient(180deg, var(--panel-beige) 0%, var(--panel-beige) 50%, var(--panel-deep) 52%, var(--panel-beige) 64%, var(--floor-light) 100%);
  }
  .wordmark {
    position: absolute;
    font-family: "PT Sans Narrow", "Arial Narrow", sans-serif;
    font-weight: 700;
    color: var(--ink);
    line-height: 1;
    letter-spacing: 0.5px;
  }
  .card-front .wordmark {
    left: 180px;
    top: 142px;
    font-size: 86px;
  }
  .card-back .wordmark {
    left: 16px;
    top: 14px;
    font-size: 86px;
  }
  .contact {
    position: absolute;
    left: 200px;
    top: 224px;
    display: grid;
    grid-template-columns: 182px auto;
    column-gap: 13px;
    row-gap: 1px;
    font-family: "Lato", "Gill Sans", sans-serif;
    font-size: 13px;
    line-height: 16px;
    color: var(--ink);
  }
  .contact dt {
    text-align: right;
    font-weight: 400;
  }
  .contact dd {
    font-weight: 700;
  }
</style>
</head>
<body>
  <main class="canvas">
    <section class="card card-front">
      <div class="room-image" role="img" aria-label="Photograph of an empty, sunlit interior room with white walls and pale wooden floorboards"></div>
      <div class="wordmark">Ostrevo</div>
    </section>

    <section class="card card-back">
      <div class="room-image" role="img" aria-label="Photograph of an empty interior room overlaid with translucent beige architectural panels"></div>
      <div class="wordmark">Ostrevo</div>
      <dl class="contact">
        <dt>Name:</dt><dd>Mira Ostrini Kalwani</dd>
        <dt>Position:</dt><dd>Arquitecto</dd>
        <dt>Cell Phone :</dt><dd>+56 9 55501234</dd>
        <dt>E-mail address:</dt><dd>emostrini@ostrevo-studio.example</dd>
        <dt>website URL:</dt><dd>www.ostrevo-studio.example</dd>
      </dl>
    </section>
  </main>
</body>
</html>
```